CBD Boutique Business Card Needed

We are in need of a business card to reflect the direction of our latest products. We are a fully organic company in which our store and products are very heavy in wood and "natural" components. We decided to bring color into one of our brands and immediately knew this is where we needed to go.

We are NOT a cash grab CBD company. We could have done this wrong, slapped a label on a shit product and left it like that. I am passionate about sharing my experience with other veterans and opening a store and making it a comfortable place for others to come and see if they can have the same experience.

Target Market(s)

We are a dual market company. We do have a beauty line that will cover the costs of the majority of our business. But we also heavily cater to veterans and first responders. I am a veteran and this is how I found out about CBD. So the marketing needs to bring in our higher end beauty clientele but also be able to not put off our customers that readily need this.

Contact Information for Business Card

What we are looking for is a light, professional, boutique design that is is neither quite feminine or masculine. Attached is a picture of a store in Portland that we asked our store designer to get her inspiration from. But all natural wood and black outlines are what is mostly in there.

Attached are the following files:

Logo: An AI file with how we have our logo. I do not understand AI and have no idea why the letters are individual. The font is Adam. OLU is the logo and Tonics of Vigor is our tagline.

KM Vantage (front and back) cards I did originally found at a trade show that I absolutely loved...while it is mostly there and I would still be happy with them but it is me pretending to be you. I understand I am not and there is probably a lot wrong that all of you would see instantly and this is why I am here.

Dropper Bottle: This is our final product mock up

Water Color: I am semi flexible here. This water color is slightly different on every level of our brand. The color itself can change...we are not stuck on THIS particular one. If you happen to make a new one that is similar in style and we use it...then I will happily commission you to change the rest on our next product run. I am pretty sure you can use this statement as evidence later . =) .

But seriously, we heavily believe in pay it forward and will work with anyone here that may have a vision bigger than ours. The winner of this contest will get preferential consideration on our marketing materials (need letterhead etc. next, as well as a brochure, and website) so three more projects coming down the pipeline.

Information to use for your mockup is contained on the card images I have included. I would prefer CBD for wellness CBD for life to be more prominent. No where else on the card do we have CBD mentioned.

Font styles to use
Sans Serif

Colors

Designer to choose colors to be used in the design.

Requirements
Must have
• Double Sided
• Front: OLU logo on front of card will be raised embossed. Background is watercolor. One has been provided. Others are up for consideration. If the rest of your design is incredible and I don't like your watercolor I will just ask to swap it.
• Back: Standard information. Not stuck on anything here. I LOVE clean minimal designs. The bleed on the card I provided is a luxury...
• Font for title and OLU is Adam. Everything else I prefer san serif or as clean as possible.
Nice to have
• I Need to incorporate Naturally Nurturing somewhere on the card. Bold but not intrusive.

```html
<!DOCTYPE html>
<html lang="en">
<head>
<meta charset="utf-8">
<title>OLU – Business Card</title>
<link rel="stylesheet" href="https://fonts.googleapis.com/css2?family=Nunito+Sans:wght@300;400;800&display=swap">
<style>
  :root {
    --page: #ffffff;
    --paper: #e4e4e4;
    --blush: #ecbfc3;
    --sage: #2f7d62;
    --ink: #1a1a1a;
    --light: #ffffff;
  }
  html, body {
    margin: 0;
    width: 1200px;
    height: 848px;
    overflow: hidden;
    background: var(--page);
    font-family: "Nunito Sans", sans-serif;
  }
  .card {
    position: absolute;
    left: 379px;
    width: 445px;
    height: 247px;
    overflow: hidden;
    background: var(--paper);
  }
  .card--front { top: 116px; }
  .card--back { top: 447px; }

  .watercolor {
    position: absolute;
    inset: 0;
  }
  .watercolor--front {
    background: linear-gradient(100deg,
      var(--blush) 0%, var(--blush) 44%,
      var(--sage) 54%, var(--sage) 62%,
      var(--paper) 68%, var(--paper) 100%);
  }
  .watercolor--back {
    background: linear-gradient(90deg,
      var(--paper) 0%, var(--paper) 7%,
      var(--blush) 9%, var(--blush) 17%,
      var(--paper) 20%, var(--paper) 34%,
      var(--sage) 50%, var(--sage) 100%);
  }

  .wordmark {
    position: absolute;
    left: 140px;
    width: 164px;
    top: 74px;
    text-align: center;
    color: var(--ink);
  }
  .wordmark__name {
    display: block;
    font-weight: 300;
    font-size: 88px;
    line-height: 88px;
    letter-spacing: 2px;
  }
  .wordmark__tagline {
    display: block;
    margin-top: 2px;
    font-weight: 300;
    font-size: 15px;
    line-height: 18px;
    letter-spacing: 1px;
    text-transform: uppercase;
    white-space: nowrap;
  }

  .slogan {
    position: absolute;
    left: 19px;
    top: 114px;
    margin: 0;
    font-size: 16px;
    line-height: 19px;
    color: var(--ink);
  }

  .contact {
    position: absolute;
    right: 9px;
    margin: 0;
    text-align: right;
    color: var(--light);
    white-space: nowrap;
  }
  .contact--name {
    top: 18px;
    font-weight: 800;
    font-size: 25px;
    line-height: 28px;
  }
  .contact--role {
    top: 50px;
    font-size: 16px;
    line-height: 20px;
    letter-spacing: 0.5px;
  }
  .contact--address,
  .contact--phone,
  .contact--mail {
    font-size: 17px;
    line-height: 19px;
  }
  .contact--address { top: 81px; }
  .contact--phone { top: 155px; }
  .contact--mail { top: 194px; }

  .icon {
    position: absolute;
    fill: none;
    stroke: var(--light);
    stroke-width: 1.6;
  }
  .icon--pin { left: 243px; top: 83px; fill: var(--light); stroke: none; }
  .icon--phone { left: 294px; top: 158px; }
  .icon--mail { left: 294px; top: 201px; }
</style>
</head>
<body>

<section class="card card--front">
  <div class="watercolor watercolor--front" role="img" aria-label="Blush pink and sage green watercolor wash on textured paper"></div>
  <div class="wordmark">
    <span class="wordmark__name">OLU</span>
    <span class="wordmark__tagline">Tonics of Vigor</span>
  </div>
</section>

<section class="card card--back">
  <div class="watercolor watercolor--back" role="img" aria-label="Sage green dry-brush watercolor sweep with a faint blush stroke on textured paper"></div>

  <p class="slogan">Hemp for balance<br>Hemp for life</p>

  <h1 class="contact contact--name">DANA WHITFIELD</h1>
  <p class="contact contact--role">OWNER/CEO</p>

  <svg class="icon icon--pin" width="14" height="20" viewBox="0 0 16 22" aria-hidden="true">
    <path d="M8 0a8 8 0 0 0-8 8c0 6 8 14 8 14s8-8 8-14a8 8 0 0 0-8-8zm0 11a3 3 0 1 1 0-6 3 3 0 0 1 0 6z"/>
  </svg>
  <p class="contact contact--address">4120 N Cedar Ridge Rd<br>Mesa, AZ 85201<br>Suite 200</p>

  <svg class="icon icon--phone" width="20" height="19" viewBox="0 0 22 20" aria-hidden="true">
    <path d="M4 2l3 0 2 5-2 1.5c1 2.5 3 4.5 5.5 5.5L14 12l5 2v3c0 1-1 2-2 2C9 19 2 12 2 4c0-1 1-2 2-2z"/>
    <path d="M13 3a5 5 0 0 1 5 5M13 6a2 2 0 0 1 2 2"/>
  </svg>
  <p class="contact contact--phone">555.014.2288</p>

  <svg class="icon icon--mail" width="22" height="16" viewBox="0 0 22 16" aria-hidden="true">
    <rect x="1" y="1" width="20" height="14"/>
    <path d="M1 1l10 8 10-8M1 15l7-6M21 15l-7-6"/>
  </svg>
  <p class="contact contact--mail">hello@olu.life<br>www.olu.life</p>
</section>

</body>
</html>
```